Criação de Papelaria Profissional para Contabilidade & Finanças
" ESTOU INICANDO AGORA O ESCRITORIO DE CONTABILIDADE, QUERO ATUAR NO RAMO DE TREINAMENTO ATRAVÉS DO COACHING , FAZER CONSULTORIAS NA AREA CONTABIL, SERVIÇOS CONTABEIS EM GERAL, DESDE O MICROEMPREENDEDOR ATÉ O A EMPRESA DE GRANDE PORTE LUCRO REAL "

```html
<!DOCTYPE html>
<html lang="pt-BR">
<head>
<meta charset="utf-8">
<title>Veltra – Banner Contabilidade</title>
<link href="https://fonts.googleapis.com/css2?family=Montserrat:wght@600;700;800&display=swap" rel="stylesheet">
<style>
  :root {
    --page-bg: #e9e6e1;
    --navy-deep: #0b1447;
    --navy: #14237a;
    --blue-mid: #24389e;
    --blue-soft: #3a52b8;
    --photo-light: #6f7fc4;
    --gold: #d8b24a;
    --white: #ffffff;
  }
  html, body {
    margin: 0;
    padding: 0;
    width: 1200px;
    height: 1200px;
    overflow: hidden;
    background: var(--page-bg);
  }
  .canvas {
    position: relative;
    width: 1200px;
    height: 1200px;
  }
  .banner {
    position: absolute;
    left: 40px;
    top: 388px;
    width: 1120px;
    height: 425px;
    overflow: hidden;
    box-shadow: 0 10px 30px rgba(0,0,0,0.25);
  }
  .banner-art {
    position: absolute;
    inset: 0;
    width: 100%;
    height: 100%;
    display: block;
  }
  .brand {
    position: absolute;
    left: 808px;
    top: 196px;
    width: 290px;
    font-family: 'Montserrat', sans-serif;
  }
  .brand-row {
    display: flex;
    align-items: center;
    gap: 14px;
  }
  .brand-mark {
    width: 34px;
    height: 34px;
    background: var(--gold);
  }
  .brand-name {
    font-size: 58px;
    font-weight: 800;
    color: var(--gold);
    letter-spacing: 1px;
    line-height: 1;
  }
  .brand-tagline {
    margin: 6px 0 0 48px;
    font-size: 11px;
    font-weight: 700;
    color: var(--gold);
    letter-spacing: 0.6px;
  }
  .website {
    position: absolute;
    left: 800px;
    top: 316px;
    font-family: 'Montserrat', sans-serif;
    font-size: 24px;
    font-weight: 700;
    color: var(--white);
  }
</style>
</head>
<body>
<div class="canvas">
  <section class="banner">
    <svg class="banner-art" viewBox="0 0 1120 425" xmlns="http://www.w3.org/2000/svg">
      <defs>
        <linearGradient id="photoTone" x1="0" y1="0" x2="1" y2="1">
          <stop offset="0" stop-color="var(--photo-light)"/>
          <stop offset="0.5" stop-color="var(--blue-soft)"/>
          <stop offset="1" stop-color="var(--navy)"/>
        </linearGradient>
      </defs>
      <rect width="1120" height="425" fill="var(--navy-deep)"/>
      <rect role="img" aria-label="Fotografia de profissional de negócios segurando uma caneta sobre documentos e gráficos, em tom azul" width="1000" height="425" fill="url(#photoTone)"/>
      <polygon points="0,0 360,0 0,260" fill="var(--blue-mid)" opacity="0.45"/>
      <polygon points="0,425 0,300 420,425" fill="var(--navy)" opacity="0.55"/>
      <polygon points="560,425 1000,0 1120,0 1120,425" fill="var(--navy-deep)"/>
      <polygon points="470,425 900,0 960,0 530,425" fill="var(--navy)" opacity="0.5"/>
    </svg>
    <div class="brand">
      <div class="brand-row">
        <span class="brand-mark"></span>
        <span class="brand-name">Veltra</span>
      </div>
      <div class="brand-tagline">CONSULTORIA CONTÁBIL &amp; FISCAL</div>
    </div>
    <div class="website">www.veltra.com.br</div>
  </section>
</div>
</body>
</html>
```